Web & Logo Design Project

STOP...please read entire brief before submitting :)
(designers have been submitting random designs)

Global Craft Mobility Network USA seeks new website.
NorvaleArc.example

Who we are: A brand new company that brings top student designers to Los Angeles for the summer to learn English and intern at some of the best design firms in Hollywood.

Clients: Students aged 19-25 and their parents

Objectives: A professional and creative site that communicates design, education, and a 4 star experience.

- Should be professional so that students trust the company
- Should encourage students to apply
- Needs to communicate creativity & design
- Should focus on the professional design studio experience and the location: Los Angeles & Hollywood!

What we need: Logo + Website

Logo should work small as a favicon and large when used on posters.
It should have an icon and the words NORVALE ARC.
Icon should work with and without the words.
Logo can be an abstract shape or a stylized light bulb.
A folder of possible logo ideas can be downloaded below.
Red White & Blue can be used, or stars. Eventually we will add other countries so logo should be able to change accordingly.

Website MUST have an animated slideshow of design pictures and location shots for the landing page. It should give students and idea of what to expect on the program. Please select your favorite pics from all of the photos attached.

Site should also be easy to maintain and optimize.
Should be easy to upload photos and add companies to the company page.

Please submit:

Logo
Landing Page
The Program Page
The Companies Page

Winner of the project will be asked to program the entire site an upload site to the server. We would also like to work with the designer in the future to upload and change the site. The final site will be in 3 languages (French, English, Spanish).

Other sites in our industry:
www.trellimarkcohort.example
www.brightwaveplacements.example

Files Provided:
Web layout in PDF format
Sample photos. (We encourage you to source additional photos.)
Logo examples
Website text in word doc. (coming soon)

If you have any questions please feel free to message us.

Target Market(s)

Students 19-25 and their parents

Industry/Entity Type

Education

Requirements
Must have
• Please use the Web Layout PDF provided and the content doc instead of lorem ipsum or Greek text with random buttons and navigation.

Animated slideshow of project photos on landing page.
Application form, Employer form, contact form
Should not have
• Should not look like an American flag. A nod to the fact that we are bringing students to the US for the summer is great, but this is not a political website. This is a site for designers that want to travel and experience Hollywood.

```html
<!DOCTYPE html>
<html lang="en">
<head>
<meta charset="utf-8">
<title>Shape Your Path — Design Internships in Hollywood</title>
<link rel="stylesheet" href="https://fonts.googleapis.com/css2?family=Open+Sans:ital,wght@0,400;0,600;0,700;0,800;1,400;1,600;1,700&family=Roboto+Condensed:wght@400;700&display=swap">
<style>
:root{
  --red:#a3121a;
  --red-dark:#7d0d12;
  --red-text:#b5121b;
  --navy:#0f1a3d;
  --navy-deep:#0a1230;
  --page:#ececec;
  --card:#d6d6d6;
  --ink:#2b2b2b;
  --muted:#7a7a7a;
  --link:#1d4f9c;
  --white:#ffffff;
}
*{box-sizing:border-box;margin:0;padding:0}
html,body{width:818px;height:1200px;overflow:hidden}
body{position:relative;background:var(--page);font-family:"Open Sans",Arial,sans-serif;color:var(--ink)}
.abs{position:absolute}

/* header */
.top-band{left:0;top:0;width:818px;height:60px;background:linear-gradient(#b3161e,var(--red-dark))}
.lang{left:570px;top:9px;width:50px;height:17px;background:#8d0f15;border-radius:2px;display:flex;gap:4px;padding:4px 6px}
.flag{width:10px;height:8px}
.flag-fr{background:linear-gradient(90deg,#24408e 33%,#fff 33% 66%,#d0202b 66%)}
.flag-es{background:linear-gradient(#c60b1e 25%,#ffc400 25% 75%,#c60b1e 75%)}
.flag-uk{background:#2a3d8f;border:1px solid #fff}
.contact-top{left:630px;top:9px;width:62px;height:17px;background:#8d0f15;border-radius:2px;color:#fff;font-size:8px;line-height:17px;padding-left:6px}
.contact-top::before{content:"";display:inline-block;width:9px;height:6px;background:#fff;margin-right:4px;vertical-align:0}
.hero{left:0;top:60px;width:818px;height:291px;background:linear-gradient(90deg,#1a1712 0%,#3b2f22 30%,#2a2620 55%,#6d6a66 70%,#3a332a 100%)}
.logo-box{left:95px;top:7px;width:122px;height:72px;background:var(--white);box-shadow:0 1px 3px rgba(0,0,0,.3);z-index:3}
.logo-dot{left:50px;top:9px;width:20px;height:20px;border-radius:50%;background:var(--red)}
.logo-name{left:0;top:52px;width:122px;text-align:center;font-size:9.5px;color:var(--red-text);font-weight:600;letter-spacing:.3px}
.nav{left:217px;top:39px;width:506px;height:40px;background:linear-gradient(#fafafa,#dcdcdc);display:flex;align-items:center;box-shadow:0 1px 3px rgba(0,0,0,.3);z-index:2}
.nav a{font-family:"Roboto Condensed",Arial,sans-serif;font-weight:700;font-size:10.5px;color:#333;text-decoration:none;display:flex;align-items:center;gap:6px;height:40px;padding:0 12px}
.nav a.active{background:#e4e4e4;border-bottom:3px solid var(--red);margin-left:75px}
.nav svg{width:10px;height:10px}
.hero-title{left:105px;top:187px;color:#fff;font-weight:800;font-size:30px;line-height:35px;letter-spacing:.3px;text-shadow:0 2px 4px rgba(0,0,0,.6)}
.hero-title small{font-size:22px}
.learn-btn{left:106px;top:286px;width:93px;height:28px;background:var(--white);color:var(--red-text);font-weight:600;font-size:11px;line-height:28px;text-align:center}
.dots{left:363px;top:341px;width:93px;height:21px;background:linear-gradient(#333,#0d0d0d);border-radius:0 0 5px 5px;display:flex;gap:8px;justify-content:center;align-items:center}
.dots span{width:8px;height:8px;border-radius:50%;background:#555}
.dots span:first-child{background:#ddd}

/* intro */
.rule{left:100px;width:618px;height:1px;background:#d6d6d6}
.intro-head{left:100px;top:389px;font-size:12.5px;font-weight:700;font-style:italic;color:#1a2450;white-space:nowrap}
.intro-head em{color:var(--red-text)}
.intro-sub{left:100px;top:406px;width:434px;font-size:8.4px;color:#444;white-space:nowrap}
.consult-btn{left:542px;top:389px;width:174px;height:32px;background:var(--red);border:2px solid #d9d9d9;color:#fff;font-size:11.5px;font-weight:600;line-height:28px;text-align:center}
.consult-btn b{color:#ffd23b}

/* cards */
.card{top:475px;width:146px;height:181px;background:linear-gradient(#dedede,#cfcfcf);text-align:center}
.card.first{background:linear-gradient(#c8c8c8,#d9d9d9)}
.card-icon{position:absolute;left:39px;top:-28px;width:68px;height:68px;border-radius:50%;background:#fff;box-shadow:0 1px 3px rgba(0,0,0,.2);display:flex;align-items:center;justify-content:center}
.card-icon svg{width:30px;height:30px}
.card-kicker{margin-top:53px;font-family:"Roboto Condensed",Arial,sans-serif;font-size:11.5px;color:#333}
.card-title{font-family:"Roboto Condensed",Arial,sans-serif;font-weight:700;font-size:25px;line-height:24px;color:#2a2a2a}
.card-text{margin:10px auto 0;width:132px;font-size:8px;line-height:12px;color:var(--muted)}
.card-go{position:absolute;left:62px;top:150px;width:22px;height:22px;border-radius:50%;background:#fff;color:#333;font-size:11px;line-height:21px}
.first .card-go{background:var(--red);color:#fff}

/* quote */
.quote-band{left:0;top:684px;width:818px;height:76px;background:#dcdcdc;border-top:1px solid #cacaca;border-bottom:1px solid #cacaca}
.avatar{left:100px;top:695px;width:57px;height:57px;border-radius:50%;background:#fff;padding:4px;box-shadow:0 1px 2px rgba(0,0,0,.2)}
.avatar div{width:100%;height:100%;border-radius:50%;background:linear-gradient(#3a2f2a,#b89c8c)}
.quote-mark{font-family:Georgia,serif;font-size:36px;color:#bdbdbd;line-height:1}
.quote-text{left:189px;top:704px;width:520px;font-style:italic;font-size:10.5px;line-height:15px;color:#555}
.quote-close{font-family:Georgia,serif;font-style:normal;font-size:30px;color:#bdbdbd;line-height:0;vertical-align:-12px;margin-left:3px}
.q-nav{top:738px;width:13px;height:13px;border-radius:50%;font-size:8px;color:#fff;text-align:center;line-height:13px}

/* featured */
.section-title{font-size:10px;font-weight:700;color:var(--red-text)}
.video{left:99px;top:806px;width:294px;height:123px;background:linear-gradient(120deg,#2c2a27,#6a5f55 40%,#8fa2b8 70%,#3d3d3d)}
.play{left:225px;top:853px;width:36px;height:36px;border-radius:50%;background:rgba(0,0,0,.55)}
.play::after{content:"";position:absolute;left:14px;top:11px;border-left:10px solid #fff;border-top:7px solid transparent;border-bottom:7px solid transparent}
.slider{left:99px;top:936px;width:294px;height:13px;background:repeating-linear-gradient(45deg,#ddd 0 2px,#ececec 2px 4px)}
.slider-arrow{top:0;width:22px;height:13px;background:#3a3a3a;color:#fff;font-size:9px;text-align:center;line-height:13px}
.slider-ticks{left:76px;top:5px;width:140px;height:3px;background:#c6c6c6}
.slider-ticks i{position:absolute;left:36px;top:0;width:17px;height:3px;background:var(--red)}

.tuition{left:414px;top:789px;width:304px;height:160px;background:#fafafa;border:1px solid #dedede}
.tuition-head{height:22px;background:#505050;color:#fff;font-size:10px;font-weight:700;line-height:22px;padding-left:10px;position:relative}
.tuition-head span{position:absolute;top:0;width:23px;height:22px;background:#2e2e2e;border-left:1px solid #666}
.tuition-head svg{width:10px;height:10px;margin:6px}
.t-item{padding:0 10px;font-size:8px;line-height:13.5px;color:#444}
.t-item h4{font-size:9.5px;font-weight:400;color:var(--red-text);margin-bottom:2px}
.t-item a{color:var(--link);text-decoration:none}

/* partners + footer */
.footer{left:0;top:1014px;width:818px;height:186px;background:var(--navy);border-top:3px solid var(--red)}
.partners{left:160px;top:989px;width:498px;height:59px;background:#fff;box-shadow:0 1px 4px rgba(0,0,0,.3);display:flex;align-items:center;justify-content:space-around;padding:0 12px}
.partner{font-family:"Open Sans",Arial,sans-serif;font-weight:700;font-size:15px;color:#4a4a4a;display:flex;align-items:center;gap:5px}
.partner i{display:block;width:24px;height:24px;border-radius:50%;border:2px solid #e88a5c}
.partner-badge{width:36px;height:36px;background:#e01e26}
.f-head{font-size:10px;font-weight:600;color:#e03535}
.f-links{font-size:8px;line-height:14px;color:#d8d8e4;list-style:none}
.f-links li::before{content:"›";color:#e03535;margin-right:4px}
.f-links li.hot{color:#e03535}
.social{display:flex;gap:4px}
.social span{width:14px;height:14px;border-radius:50%;background:#5c7fb5}
.fb-btn{height:15px;padding:0 5px;background:#eef0f6;border:1px solid #a8b4cc;font-size:7px;line-height:13px;color:#3b5998}
.f-brand{left:598px;top:1116px;width:120px;text-align:center;font-size:10px;font-weight:600;color:var(--red-text)}
.f-brand-dot{left:652px;top:1078px;width:20px;height:20px;border-radius:50%;background:var(--red)}
.bottom-bar{left:0;top:1157px;width:818px;height:43px;background:var(--navy-deep);border-top:1px solid #1d2a55;text-align:center;font-size:8px;color:#c9cbd6;line-height:40px}
.bottom-bar a{color:#5a8ad0;text-decoration:none}
</style>
</head>
<body>

<header>
  <div class="abs top-band"></div>
  <div class="abs lang"><span class="flag flag-fr"></span><span class="flag flag-es"></span><span class="flag flag-uk"></span></div>
  <div class="abs contact-top">Contact Us</div>
  <div class="abs hero" role="img" aria-label="Night skyline of downtown Los Angeles with two smiling young professionals in office wear"></div>

  <div class="abs logo-box">
    <div class="abs logo-dot"></div>
    <div class="abs logo-name">SHAPE YOUR PATH</div>
  </div>

  <nav class="abs nav">
    <a class="active" href="#"><svg viewBox="0 0 10 10"><rect x="0.5" y="1.5" width="8" height="8" fill="none" stroke="#333"/><path d="M2 5l2 2 5-6" fill="none" stroke="#333" stroke-width="1.5"/></svg>APPLY</a>
    <a href="#"><svg viewBox="0 0 10 10"><path d="M8.5 4A3.5 3.5 0 1 0 8 7" fill="none" stroke="#555" stroke-width="1.4"/><path d="M9.5 1v3.5H6z" fill="#555"/></svg>MISSION</a>
    <a href="#"><svg viewBox="0 0 10 10"><rect x="0.5" y="3" width="9" height="6" fill="#555"/><rect x="3" y="1" width="4" height="2.5" fill="none" stroke="#555"/></svg>THE PROGRAM</a>
    <a href="#"><svg viewBox="0 0 10 10"><path d="M1 9l1-3 5-5 2 2-5 5z" fill="#555"/></svg>THE COMPANIES</a>
    <a href="#"><svg viewBox="0 0 10 10"><text x="2" y="9" font-size="10" font-weight="700" fill="#555" font-family="Arial">?</text></svg>FAQ</a>
  </nav>

  <h1 class="abs hero-title">SECURE <small>A TOP</small> DESIGN<br>INTERNSHIP</h1>
  <div class="abs learn-btn">LEARN MORE</div>
  <div class="abs dots"><span></span><span></span><span></span><span></span></div>
</header>

<main>
  <div class="abs rule" style="top:374px"></div>
  <p class="abs intro-head">Receive real world work experience, <em>improve your professional</em> portfolio</p>
  <p class="abs intro-sub">Increase your English language skills, and get a taste of what it is like to live, work, and play in Hollywood.</p>
  <div class="abs consult-btn">Contact for <b>FREE</b> Cosultaion!</div>
  <div class="abs rule" style="top:431px"></div>

  <section class="abs card first" style="left:100px">
    <div class="card-icon"><svg viewBox="0 0 30 30"><rect x="2" y="9" width="26" height="17" rx="2" fill="#c8161e"/><rect x="10" y="4" width="10" height="6" rx="1" fill="none" stroke="#c8161e" stroke-width="2"/><rect x="2" y="15" width="26" height="2" fill="#fff"/><rect x="13" y="14" width="4" height="4" fill="#fff"/></svg></div>
    <div class="card-kicker">HOW WE</div><div class="card-title">WORK</div>
    <p class="card-text">We partner with our clients to deliver the most effective campaigns with the highest ROIs while ensuring.</p>
    <div class="card-go">›</div>
  </section>
  <section class="abs card" style="left:257px">
    <div class="card-icon"><svg viewBox="0 0 30 30"><rect x="4" y="5" width="18" height="22" rx="2" fill="none" stroke="#333" stroke-width="2.5"/><rect x="9" y="2" width="8" height="5" fill="#333"/><path d="M12 20l12-12 3 3-12 12h-3z" fill="#333"/></svg></div>
    <div class="card-kicker">PERFECT</div><div class="card-title">SERVICES</div>
    <p class="card-text">We partner with our clients to deliver the most effective campaigns with the highest ROIs while ensuring.</p>
    <div class="card-go">›</div>
  </section>
  <section class="abs card" style="left:414px">
    <div class="card-icon"><svg viewBox="0 0 30 30"><path d="M11 3h8l-2 5h-4z" fill="#333"/><path d="M13 8h4l3 15-5 5-5-5z" fill="#333"/></svg></div>
    <div class="card-kicker">EXECUTIVE</div><div class="card-title">TEAM</div>
    <p class="card-text">We partner with our clients to deliver the most effective campaigns with the highest ROIs while ensuring.</p>
    <div class="card-go">›</div>
  </section>
  <section class="abs card" style="left:572px">
    <div class="card-icon"><svg viewBox="0 0 30 30"><path d="M5 16a10 10 0 0 1 20 0" fill="none" stroke="#333" stroke-width="2.5"/><circle cx="15" cy="16" r="7" fill="none" stroke="#333" stroke-width="2"/><rect x="3" y="14" width="4" height="7" rx="1" fill="#333"/><rect x="23" y="14" width="4" height="7" rx="1" fill="#333"/><path d="M25 21q0 5-7 5" fill="none" stroke="#333" stroke-width="1.5"/><circle cx="17" cy="26" r="1.5" fill="#c8161e"/></svg></div>
    <div class="card-kicker">QUICK</div><div class="card-title">SUPPORT</div>
    <p class="card-text">We partner with our clients to deliver the most effective campaigns with the highest ROIs while ensuring.</p>
    <div class="card-go">›</div>
  </section>

  <section>
    <div class="abs quote-band"></div>
    <div class="abs avatar"><div role="img" aria-label="Portrait of a smiling student with dark hair"></div></div>
    <span class="abs quote-mark" style="left:166px;top:700px">“</span>
    <blockquote class="abs quote-text">We are looking for the brightest and most dedicated student designers to come and experience firsthand what it is like to work and learn in one of the most exciting cities in the world, Los Angeles.<span class="quote-close">”</span></blockquote>
    <div class="abs q-nav" style="left:687px;background:#bbb">‹</div>
    <div class="abs q-nav" style="left:702px;background:#333">›</div>
  </section>

  <section>
    <h3 class="abs section-title" style="left:99px;top:785px">FEATURED WORKS</h3>
    <div class="abs video" role="img" aria-label="Video still of a young designer drawing a cartoon on a pen tablet screen"></div>
    <div class="abs play"></div>
    <div class="abs slider">
      <div class="abs slider-arrow" style="left:0">‹</div>
      <div class="abs slider-ticks"><i></i></div>
      <div class="abs slider-arrow" style="right:0">›</div>
    </div>
  </section>

  <section class="abs tuition">
    <div class="tuition-head">PROGRAM TUITION
      <span style="right:23px"><svg viewBox="0 0 10 10"><path d="M1 7l4-4 4 4" fill="none" stroke="#fff" stroke-width="1.2"/></svg></span>
      <span style="right:0"><svg viewBox="0 0 10 10"><path d="M1 3l4 4 4-4" fill="none" stroke="#fff" stroke-width="1.2"/></svg></span>
    </div>
    <div class="t-item" style="margin-top:11px">
      <h4>What you get</h4>
      <p>Luxury housing in the center of Hollywood (2 months)Guaranteed design internship (200-280 hours of practical design experience) ... <a href="#">Read more</a></p>
    </div>
    <div style="margin:10px 8px 12px;height:1px;background:#e0e0e0"></div>
    <div class="t-item">
      <h4>Not included</h4>
      <p>Transportation to and from work , Overnight excursions , Medical insurance Meals, Visa and/or document fees ... <a href="#">Read more</a></p>
    </div>
  </section>
</main>

<footer>
  <div class="abs footer"></div>
  <div class="abs partners">
    <span class="partner"><i></i>Kestrel</span>
    <span class="partner">Halden Row</span>
    <span class="partner" style="font-size:12px;color:#5a9a2a">Brightmoss</span>
    <span class="partner-badge"></span>
    <span class="partner" style="color:#222">Orlo Studio</span>
  </div>

  <h4 class="abs f-head" style="left:103px;top:1070px">QUICK LINKS</h4>
  <ul class="abs f-links" style="left:103px;top:1090px"><li class="hot">Apply</li><li>Mission</li><li>The Program</li></ul>
  <ul class="abs f-links" style="left:203px;top:1090px"><li>The Companies</li><li>FAQ</li><li>Contact</li></ul>
  <ul class="abs f-links" style="left:308px;top:1090px"><li>Legal</li></ul>
  <div class="abs" style="left:354px;top:1070px;width:1px;height:70px;background:#26336a"></div>

  <h4 class="abs f-head" style="left:372px;top:1070px">CONNECTED WITH US</h4>
  <div class="abs social" style="left:372px;top:1091px"><span></span><span></span><span></span><span></span></div>
  <div class="abs" style="left:373px;top:1120px;display:flex;gap:5px;align-items:center">
    <span class="fb-btn">Like</span><span class="fb-btn">Send</span>
    <span style="font-size:7px;color:#d8d8e4">1,009,575 people like this.</span>
  </div>

  <div class="abs f-brand-dot"></div>
  <div class="abs f-brand">SHAPE YOUR PATH</div>

  <div class="abs bottom-bar">© Copyright Shape Your Path, Inc 2012. All Rights Reserved. <a href="#">Privacy Policy</a> | <a href="#">Terms &amp; Conditions</a></div>
</footer>

</body>
</html>
```